Bramwell Joinery Website

My client Bramwell Joinery is looking for a redesign for a Word Press Website. Their current site is at www.bramwelljoinery.example They are a custom cabinet company, but also create bathroom, living room, bar and entertainment and bedroom cabinets too. They would like a design that emulates the master craftsman work they do yet a contemporary style.

Their current site was designed using Flash elements.

Target Market(s)

Home owners and builders of high end homes

Industry/Entity Type

Entertainment

Font styles to use
Serif
Decorative

Requirements
Must have
• Must show their work and logo using a contemporary style.
Nice to have
• Sliders that showcase their projects.

```html
<!DOCTYPE html>
<html lang="en">
<head>
<meta charset="utf-8">
<title>Bramwell Joinery</title>
<link href="https://fonts.googleapis.com/css2?family=Oswald:wght@400;600;700&family=Lato:wght@400;700&family=Arimo:wght@400;700&display=swap" rel="stylesheet">
<style>
:root{
  --green:#3fae3a;
  --ink:#222;
  --text:#555;
  --muted:#8a8a8a;
  --grey-band:#e6e6e6;
  --white:#fff;
  --line:#dcdcdc;
  --navy:#1d1f2b;
}
*{margin:0;padding:0;box-sizing:border-box}
html,body{width:1200px;height:2282px;overflow:hidden}
body{position:relative;background:var(--white);font-family:"Lato",sans-serif;color:var(--text)}
.abs{position:absolute}

/* header */
.site-header{left:0;top:0;width:1200px;height:122px;background:var(--white);border-top:4px solid var(--green)}
.logo{left:158px;top:18px;width:88px;height:88px;border-radius:50%;border:4px solid var(--green);display:flex;align-items:center;justify-content:center;text-align:center;font-family:"Oswald",sans-serif;font-size:13px;line-height:1.1;color:var(--green);font-weight:600}
.social-badge{left:735px;top:42px;width:142px;height:42px;background:#dfe3ea;border:1px solid #b8bfcc;border-radius:3px}
.question{left:893px;top:38px;font-family:"Arimo",sans-serif;font-size:13px;color:#333}
.phone{left:891px;top:54px;font-family:"Oswald",sans-serif;font-weight:600;font-size:29px;color:var(--green);letter-spacing:.5px}

/* hero */
.hero-band{left:0;top:122px;width:1200px;height:418px;background:linear-gradient(90deg,#0e0e0e,#242424 30%,#161616 60%,#262626 85%,#111)}
.main-nav{left:152px;top:148px;width:894px;height:47px;background:var(--white);display:flex;align-items:stretch;font-family:"Arimo",sans-serif;font-size:11.5px;color:#333;text-transform:uppercase;overflow:hidden}
.main-nav span{flex:1 1 auto;display:flex;align-items:center;justify-content:center;padding:0 7px;border-right:1px solid #ddd;white-space:nowrap}
.main-nav .active{background:var(--green);color:var(--white);font-weight:700}
.main-nav .last{border-right:none}
.main-nav .search{flex:0 0 46px;background:var(--green);padding:0;border:none}
.slider{left:152px;top:195px;width:894px;height:405px;border-bottom:3px solid #7a1414;background:linear-gradient(180deg,#6a4423 0%,#9b6a3a 35%,#b59c80 52%,#8a5a30 70%,#5a3618 100%)}
.slide-arrow{top:385px;width:46px;height:46px;border-radius:50%;background:rgba(0,0,0,.45);border:2px solid rgba(255,255,255,.7)}
.slide-title{left:152px;top:450px;width:894px;text-align:center;font-family:"Oswald",sans-serif;font-weight:700;font-size:41px;line-height:56px;color:var(--white);text-shadow:0 2px 4px rgba(0,0,0,.6)}
.slide-sub{left:152px;top:506px;width:894px;text-align:center;font-family:"Arimo",sans-serif;font-size:18px;line-height:22px;color:var(--white);text-shadow:0 1px 3px rgba(0,0,0,.7)}
.dots{left:546px;top:556px;display:flex;gap:5px}
.dots i{width:14px;height:14px;border-radius:50%;background:#ccc;border:1px solid #888}
.dots i.on{background:var(--green)}

.tagline{left:0;top:627px;width:1200px;text-align:center;font-family:"Arimo",sans-serif;font-size:27px;line-height:38px;color:#333}
.tagline em{font-style:normal;color:var(--green)}

/* offer */
.offer{left:0;top:727px;width:1200px;height:303px;background:var(--grey-band)}
.section-title{font-family:"Lato",sans-serif;font-weight:400;font-size:23px;color:#222;letter-spacing:.5px}
.offer-title{left:0;top:770px;width:1200px;text-align:center}
.services{left:180px;top:820px;width:850px;display:flex;justify-content:space-between}
.service{display:flex;flex-direction:column;align-items:center;gap:10px;font-family:"Lato",sans-serif;font-size:16px;color:#333;text-transform:uppercase;width:120px;white-space:nowrap}
.service svg{width:48px;height:48px}
.service.current{color:var(--green)}
.offer-copy{left:180px;top:920px;width:850px;text-align:center;font-size:13.5px;line-height:22px;color:var(--muted);letter-spacing:.5px}

/* news + gallery */
.news-title{left:160px;top:1076px}
.gallery-title{left:438px;top:1076px}
.news-list{left:160px;top:1120px;width:252px}
.news-item{display:flex;gap:10px;padding:10px 0 12px;border-bottom:1px solid var(--line);height:76px}
.news-thumb{width:52px;height:44px;flex:none;background:linear-gradient(135deg,#8c7a66,#cfc2b0)}
.news-item h4{font-family:"Arimo",sans-serif;font-size:12.5px;color:#222;font-weight:700;margin-bottom:3px}
.news-item p{font-size:11px;line-height:14px;color:#666}
.btn{height:30px;font-family:"Lato",sans-serif;font-size:13px;color:var(--white);display:flex;align-items:center;justify-content:center;text-transform:uppercase}
.btn-green{left:163px;top:1350px;width:128px;background:var(--green)}
.btn-navy{left:440px;top:1350px;width:128px;background:var(--navy)}
.gallery{left:438px;top:1117px;width:602px;display:grid;grid-template-columns:repeat(3,193px);grid-auto-rows:100px;gap:16px 11px}
.gallery div{border-radius:3px;background:linear-gradient(160deg,#e5e1da,#8b8377 55%,#3c3833)}
.gallery div:nth-child(2n){background:linear-gradient(160deg,#d7d2ca,#6d655a 55%,#25211d)}
.divider{left:160px;top:1428px;width:880px;height:1px;background:var(--line)}

/* testimonials + clients */
.testi-title{left:160px;top:1462px}
.clients-title{left:598px;top:1462px}
.avatar{left:160px;top:1508px;width:70px;height:66px;background:linear-gradient(180deg,#8a6a55,#d4b9a3)}
.quote{left:248px;top:1508px;width:328px;height:120px;background:#e3e3e3;border-radius:6px;padding:14px 16px;font-size:11.5px;line-height:16px;font-style:italic;color:#444;text-align:center}
.quote-author{left:258px;top:1640px;font-size:13px;font-style:italic;color:#333}
.clients{left:598px;top:1508px;width:445px;display:grid;grid-template-columns:repeat(3,1fr);grid-auto-rows:78px;align-items:center}
.clients span{font-family:"Oswald",sans-serif;font-weight:600;font-size:32px;color:#111}

/* hello */
.hello{left:0;top:1705px;width:1200px;height:252px;background:var(--grey-band)}
.hello-title{left:0;top:1762px;width:1200px;text-align:center;font-family:"Oswald",sans-serif;font-weight:700;font-size:34px;color:#222}
.hello-copy{left:180px;top:1812px;width:840px;text-align:center;font-size:13.5px;line-height:20px;color:var(--muted)}
.social{left:514px;top:1865px;display:flex;gap:17px}
.social i{width:38px;height:38px;border-radius:50%;border:2px solid var(--white);box-shadow:0 0 0 1px #bbb}

/* footer */
.footer-line{left:0;top:1957px;width:1200px;height:5px;background:var(--green)}
.footer{left:0;top:1962px;width:1200px;height:320px;background:linear-gradient(90deg,#101010,#1f1f1f 40%,#141414 70%,#202020)}
.footer-heading{font-family:"Lato",sans-serif;font-weight:700;font-size:17px;color:var(--white);text-transform:uppercase}
.f-about-title{left:163px;top:2003px}
.f-about{left:163px;top:2036px;width:290px;font-size:12.5px;line-height:22px;color:#ddd;font-weight:700}
.f-about em{font-style:normal;color:var(--green)}
.f-port-title{left:505px;top:2003px}
.f-port{left:505px;top:2042px;display:grid;grid-template-columns:repeat(4,54px);grid-auto-rows:44px;gap:11px 7px}
.f-port div{border:2px solid #555;background:linear-gradient(150deg,#c9c2b6,#5d554b)}
.f-contact-title{left:790px;top:2003px}
.f-contact{left:790px;top:2040px;width:260px;font-size:11.5px;line-height:17px;color:#ddd}
.f-contact b{color:var(--green)}
.contact-row{display:flex;align-items:center;gap:10px;margin-top:4px}
.contact-row svg{width:16px;height:16px;flex:none}
.f-bottom-line{left:163px;top:2243px;width:878px;height:1px;background:#444}
.f-links{left:163px;top:2256px;font-size:11px;color:#ccc}
.f-links b{color:var(--green);font-weight:400}
.f-copy{left:760px;top:2256px;width:280px;text-align:right;font-size:11px;color:#ccc}
.f-copy b{color:var(--green)}
</style>
</head>
<body>

<header class="site-header abs"></header>
<div class="logo abs">BRAMWELL<br>JOINERY</div>
<div class="social-badge abs" aria-hidden="true"></div>
<div class="question abs">Have a Question for Us?</div>
<div class="phone abs">555 014 2290</div>

<section class="hero-band abs"></section>
<nav class="main-nav abs">
  <span class="active">Home</span><span>Who We Are</span><span>Getting Started</span><span>Contact Us</span><span>Customer Experience</span><span>Professional</span><span>Portfolio</span><span class="last">Cabinet Hardware</span>
  <span class="search"><svg width="18" height="18" viewBox="0 0 18 18"><circle cx="7.5" cy="7.5" r="5.5" fill="none" stroke="#fff" stroke-width="2.2"/><line x1="11.5" y1="11.5" x2="16" y2="16" stroke="#fff" stroke-width="2.4" stroke-linecap="round"/></svg></span>
</nav>
<div class="slider abs" role="img" aria-label="Photo of a wooden kitchen with cherry cabinets and stone backsplash"></div>
<div class="slide-arrow abs" style="left:172px"><svg width="42" height="42" viewBox="0 0 42 42"><polyline points="24,13 16,21 24,29" fill="none" stroke="#fff" stroke-width="3"/></svg></div>
<div class="slide-arrow abs" style="left:982px"><svg width="42" height="42" viewBox="0 0 42 42"><polyline points="18,13 26,21 18,29" fill="none" stroke="#fff" stroke-width="3"/></svg></div>
<h1 class="slide-title abs">AFFORDABLE SOLUTIONS FOR LIVING</h1>
<p class="slide-sub abs">Style, Comfort, Quality, Selection!</p>
<div class="dots abs"><i></i><i></i><i class="on"></i><i></i><i></i></div>

<p class="tagline abs">We’ve been <em>designing and manufacturing</em><br>the Midwest’s finest <em>custom cabinets and fixtures</em> since <em>1966</em></p>

<section class="offer abs"></section>
<h2 class="section-title offer-title abs">WHAT WE OFFER</h2>
<div class="services abs">
  <div class="service"><svg viewBox="0 0 48 48"><circle cx="24" cy="24" r="12" fill="none" stroke="#333" stroke-width="3"/><line x1="6" y1="10" x2="6" y2="40" stroke="#333" stroke-width="3"/><line x1="42" y1="10" x2="42" y2="40" stroke="#333" stroke-width="3"/></svg>Kitchen</div>
  <div class="service current"><svg viewBox="0 0 48 48"><path d="M6 26h36v6a8 8 0 0 1-8 8H14a8 8 0 0 1-8-8z" fill="#3fae3a"/><path d="M12 26V10a4 4 0 0 1 8 0" fill="none" stroke="#3fae3a" stroke-width="3"/></svg>Bath</div>
  <div class="service"><svg viewBox="0 0 48 48"><rect x="8" y="30" width="32" height="4" fill="#333"/><rect x="10" y="34" width="3" height="10" fill="#333"/><rect x="35" y="34" width="3" height="10" fill="#333"/><circle cx="22" cy="14" r="5" fill="#333"/><rect x="17" y="20" width="10" height="10" fill="#333"/><rect x="29" y="16" width="9" height="13" fill="#333"/></svg>Office</div>
  <div class="service"><svg viewBox="0 0 48 48"><path d="M20 6h8v8l8 30H12l8-30z" fill="#333"/></svg>Closet/Dressing</div>
  <div class="service"><svg viewBox="0 0 48 48"><circle cx="24" cy="16" r="9" fill="none" stroke="#333" stroke-width="3"/><rect x="6" y="30" width="36" height="4" fill="#333"/><rect x="10" y="34" width="3" height="10" fill="#333"/><rect x="35" y="34" width="3" height="10" fill="#333"/></svg>Workshop</div>
  <div class="service"><svg viewBox="0 0 48 48"><rect x="8" y="28" width="32" height="4" fill="#333"/><circle cx="14" cy="14" r="4" fill="#333"/><circle cx="34" cy="14" r="4" fill="#333"/><rect x="10" y="19" width="8" height="9" fill="#333"/><rect x="30" y="19" width="8" height="9" fill="#333"/><rect x="20" y="32" width="8" height="12" fill="#333"/></svg>Entertainment</div>
</div>
<p class="offer-copy abs">Sed ut perspiciatis unde omnis iste natus error sit voluptatem accusantium doloremque laudantium, totam rem aperiam, eaque ipsa quae ab illo inventore veritatis et quasi architecto beatae vitae dicta sunt explicabo. Nemo sit voluptatem doloremque laudantium, totam ratione voluptatem sequi nesciunt.</p>

<h2 class="section-title news-title abs">RECENT NEWS</h2>
<div class="news-list abs">
  <article class="news-item"><div class="news-thumb" role="img" aria-label="News thumbnail of a cabinet project"></div><div><h4>Morbi id malesuada augu elis</h4><p>Morbi id malesuada augue,auctor ahfc nunc sit amet,, porttitor lobortis .</p></div></article>
  <article class="news-item"><div class="news-thumb" role="img" aria-label="News thumbnail of a cabinet project"></div><div><h4>Morbi id malesuada augu elis</h4><p>Morbi id malesuada augue,auctor ahfc nunc sit amet,, porttitor lobortis .</p></div></article>
  <article class="news-item" style="border:none"><div class="news-thumb" role="img" aria-label="News thumbnail of a cabinet project"></div><div><h4>Morbi id malesuada augu elis</h4><p>Morbi id malesuada augue,auctor ahfc nunc sit amet,, porttitor lobortis .</p></div></article>
</div>
<div class="btn btn-green abs">View More</div>

<h2 class="section-title gallery-title abs">OUR GALLERY</h2>
<div class="gallery abs">
  <div role="img" aria-label="White kitchen with island"></div>
  <div role="img" aria-label="Kitchen with range hood"></div>
  <div role="img" aria-label="Living room built-in cabinetry"></div>
  <div role="img" aria-label="Open-plan kitchen"></div>
  <div role="img" aria-label="Dark wood kitchen island"></div>
  <div role="img" aria-label="Dark kitchen island detail"></div>
</div>
<div class="btn btn-navy abs">View More</div>

<div class="divider abs"></div>

<h2 class="section-title testi-title abs">TESTIMONIALS</h2>
<div class="avatar abs" role="img" aria-label="Portrait of the client"></div>
<blockquote class="quote abs">“Lorem ipsum dolor sit amet, consectetur adipiscing elit, sed do eiusmod tempor incididunt ut labore et dolore magna aliqua. Ut enim ad minim veniam, quis nostrud exercitation ullamco laboris nisi ut aliquip ex ea commodo consequat. Duis aute irure dolor in reprehenderit in voluptate velit esse cillum dolore eu fugiat nulla. Excepteur sint cupidata”.</blockquote>
<p class="quote-author abs">- Anna Whitlow</p>

<h2 class="section-title clients-title abs">OUR CLIENTS</h2>
<div class="clients abs">
  <span>Larkfield</span><span>Ovena</span><span>Merrow</span>
  <span>Merrow</span><span>Tallis</span><span>Corvane</span>
</div>

<section class="hello abs"></section>
<h2 class="hello-title abs">HELLO !</h2>
<p class="hello-copy abs">Sed ut perspiciatis unde omnis iste natus error sit voluptatem accusantium doloremque laudantium, totam rem aperiam, eaque ipsa quae e natus error sit voluptab illo inventore veritatis et quasi architecto beatae vitae dicta sunt explicabo.</p>
<div class="social abs">
  <i style="background:#1f8fd6"></i><i style="background:#2f55a4"></i><i style="background:#d23a2a"></i><i style="background:#2a8a3a"></i>
</div>

<div class="footer-line abs"></div>
<footer class="footer abs"></footer>
<h3 class="footer-heading f-about-title abs">About Us</h3>
<p class="f-about abs">Established in <em>1966</em>, <em>Bramwell Joinery</em> has long stood as one of the Midwest’s most renowned makers of custom cabinets and fixtures. Our handcrafted, award-winning creations have been chosen by hundreds of noteworthy homebuilders. And while we custom build cabinets, we built our business around the belief that our customers absolutely, unequivocally come first.</p>
<h3 class="footer-heading f-port-title abs">Recent Portfolio</h3>
<div class="f-port abs">
  <div role="img" aria-label="Portfolio thumbnail"></div><div role="img" aria-label="Portfolio thumbnail"></div><div role="img" aria-label="Portfolio thumbnail"></div><div role="img" aria-label="Portfolio thumbnail"></div>
  <div role="img" aria-label="Portfolio thumbnail"></div><div role="img" aria-label="Portfolio thumbnail"></div><div role="img" aria-label="Portfolio thumbnail"></div><div role="img" aria-label="Portfolio thumbnail"></div>
  <div role="img" aria-label="Portfolio thumbnail"></div><div role="img" aria-label="Portfolio thumbnail"></div><div role="img" aria-label="Portfolio thumbnail"></div><div role="img" aria-label="Portfolio thumbnail"></div>
</div>
<h3 class="footer-heading f-contact-title abs">Contact Us</h3>
<div class="f-contact abs">
  <p>Got a question for Bramwell? We’d love to hear from you! Whether it’s for a project inquiry.</p>
  <p><b>Bramwell Joinery</b></p>
  <p>Tom Hadley, 42 Alder Row, Fenwick, MO-00000</p>
  <div class="contact-row"><svg viewBox="0 0 16 16"><circle cx="8" cy="8" r="7" fill="none" stroke="#ddd"/><path d="M5 4l2 2-1 1 3 3 1-1 2 2-1.5 1.5C7 12 4 9 3.5 5.5z" fill="#ddd"/></svg>:&nbsp; 555.010.2300</div>
  <div class="contact-row"><svg viewBox="0 0 16 16"><rect x="2" y="4" width="12" height="9" rx="1" fill="#ddd"/><rect x="4" y="2" width="8" height="3" fill="#ddd"/></svg>:&nbsp; 555.010.7835</div>
  <div class="contact-row"><svg viewBox="0 0 16 16"><rect x="1.5" y="3.5" width="13" height="9" fill="none" stroke="#ddd"/><polyline points="1.5,3.5 8,9 14.5,3.5" fill="none" stroke="#ddd"/></svg>:&nbsp; info@bramwelljoinery.example</div>
</div>
<div class="f-bottom-line abs"></div>
<p class="f-links abs"><b>Home</b> &nbsp;|&nbsp; Who Are We &nbsp;|&nbsp; Professional &nbsp;|&nbsp; Portfolio &nbsp;|&nbsp; Contact Us</p>
<p class="f-copy abs">© 2015. All rights reserved. <b>Bramwell Joinery.</b></p>

</body>
</html>
```